Clean, Corporate redesign of existing website

We require a clean corporate professional redesign of our existing poor website, although a simple and elegant structure is required we would like the designer to concentrate on the little things and finishes to give the site a highly professional feel.
The company have supplied the following websites as to use as inspiration http://www.tollardminerals.com/ they like the clean, professional feel of the website
and the fact that the website captures the feel of their industry. Another clean and professional site they liked the look of was http://www.brindlefishbites.co.uk/ .
Another inspirational (page level only) http://www.harrowgateexpohall.com/thefacilities/floor-maps-and-specifications/ we like the top image and the corporate feel the images give. Auto cad drawings as images or a search for electrical services will fetch up a good selection of images to use as placeholders
A full brief, logos, images etc have been supplied
update: the sector is industrial electrical services, so more towards factory switches and equipement, not domestic light-bulbs etc this is important when choosing images for the site.
Updates
Thank you all for your designs, i will be presenting the best to the company tomorrow who will pick the design that suits so please get any remaining designs to me by tomorrow morning (GMT time) at the latest to be included in the presentation.
Target Market(s)
Business owners and CEO'S
Industry/Entity Type
Electrical
Look and feel

```html
<!DOCTYPE html>
<html lang="en">
<head>
<meta charset="utf-8">
<title>Fenwold Electrical Services Limited</title>
<link href="https://fonts.googleapis.com/css2?family=Arimo:wght@400;700&family=Ubuntu:wght@400;500&family=PT+Sans+Narrow:wght@400;700&display=swap" rel="stylesheet">
<style>
:root{
  --bg-deep:#3f5877;
  --bg-mid:#8a8f99;
  --page:#dde1e7;
  --page-light:#eceef1;
  --brand-red:#b0141f;
  --button-red:#a8121c;
  --text:#333;
  --text-muted:#8a8e94;
  --nav-text:#555;
  --frame:#ffffff;
  --footer:#c9ccd2;
}
*{margin:0;padding:0;box-sizing:border-box}
html,body{width:1200px;height:866px;overflow:hidden}
body{
  position:relative;
  font-family:"Arimo",Arial,sans-serif;
  color:var(--text);
  background:linear-gradient(100deg,var(--bg-deep) 0%,#6f7f95 20%,var(--bg-mid) 50%,#6d7c92 80%,var(--bg-deep) 100%);
}
.page{
  position:absolute;left:241px;top:0;width:720px;height:866px;
  background:linear-gradient(180deg,var(--page) 0%,var(--page-light) 45%,#e2e4e8 100%);
  box-shadow:0 0 12px rgba(0,0,0,.35);
}
.abs{position:absolute}
.contact-bar{left:0;top:12px;width:697px;text-align:right;font-size:9px;color:var(--text-muted)}
.contact-bar span.sep{margin:0 12px}
.logo{left:21px;top:42px;color:var(--brand-red);font-family:"Ubuntu",sans-serif;font-weight:400;font-size:20px;line-height:24px}
.nav{left:246px;top:60px;display:flex;align-items:center;font-family:"Ubuntu",sans-serif;font-size:10.5px;color:var(--nav-text)}
.nav a{color:inherit;text-decoration:none;width:90px;text-align:center;line-height:30px}
.nav a.active{background:linear-gradient(#c22a33,var(--button-red));color:#fff;border-radius:3px;box-shadow:0 2px 3px rgba(0,0,0,.3)}
.slider{left:21px;top:127px;width:676px;height:226px;background:var(--frame);border-radius:12px;box-shadow:0 1px 4px rgba(0,0,0,.25)}
.slide{position:absolute;left:8px;top:8px;width:660px;height:210px;border-radius:8px;overflow:hidden;
  background:radial-gradient(ellipse at 40% 50%,#2f7a55 0%,#24573f 55%,#1c3a2c 100%)}
.slide h1{position:absolute;left:0;width:100%;text-align:center;color:#fff;font-family:"PT Sans Narrow",sans-serif;font-weight:700;text-shadow:0 2px 4px rgba(0,0,0,.5)}
.slide .l1{top:86px;font-size:36px;line-height:36px}
.slide .l2{top:120px;font-size:52px;line-height:52px}
.dots{position:absolute;right:52px;bottom:17px;display:flex;gap:3px}
.dots i{width:12px;height:12px;border:2px solid #fff;border-radius:50%}
.dots i.on{background:var(--brand-red)}
h2{font-family:"Ubuntu",sans-serif;font-weight:400;font-size:19px;color:var(--brand-red)}
.welcome{left:21px;top:383px;width:378px}
.services{left:433px;top:383px;width:264px}
.photo{background:var(--frame);border-radius:6px;padding:4px;box-shadow:0 1px 3px rgba(0,0,0,.3)}
.photo div{width:100%;height:100%;border-radius:3px}
.welcome .photo{float:left;width:106px;height:128px;margin:0 16px 14px 0}
.welcome .photo div{background:linear-gradient(160deg,#b7b3b6,#7d787c)}
.body-copy{font-size:9px;line-height:13.6px}
.welcome .intro{margin-top:21px}
.body-copy p{margin-bottom:13.6px}
.body-copy b{font-weight:700}
.badges{left:97px;top:731px;width:225px;height:45px;background:#d0d2d6;border-radius:4px;display:flex;align-items:center;justify-content:center;gap:28px}
.badges span{width:58px;height:24px;border-radius:4px;background:#a4a7ad}
.services .photo{width:264px;height:128px;margin-top:21px}
.services .photo div{background:linear-gradient(135deg,#b8bcc0,#7f8388)}
.services .lead{margin-top:15px}
.service-list{list-style:none;margin:12px 0 10px;font-size:13px;color:var(--brand-red)}
.service-list li{line-height:22.5px;padding-left:15px;position:relative}
.service-list li::before{content:"";position:absolute;left:1px;top:7px;border-left:5px solid var(--brand-red);border-top:4px solid transparent;border-bottom:4px solid transparent}
.footer{left:0;top:814px;width:720px;height:52px;background:linear-gradient(#cfd2d7,var(--footer));border-top:1px solid #b9bcc2;font-size:9px;color:#6d7177}
.footer .copy{position:absolute;left:21px;top:20px}
.footer .addr{position:absolute;left:0;width:720px;top:14px;text-align:center;line-height:13.6px}
.footer .follow{position:absolute;right:23px;top:15px;display:flex;align-items:center;gap:6px}
.footer .follow i{width:23px;height:23px;background:#1f6fa8;border-radius:3px}
</style>
</head>
<body>
<div class="page">
  <div class="abs contact-bar">Phone: 01632 960411<span class="sep">|</span>Fax: 01632 960512<span class="sep">|</span>Email: info@fenwoldelectrical.com</div>
  <div class="abs logo">Fenwold Electrical<br>Services Limited</div>
  <nav class="abs nav">
    <a class="active" href="#">Home</a><a href="#">Services</a><a href="#">Clients</a><a href="#">Responsibilities</a><a href="#">Contact</a>
  </nav>
  <div class="abs slider">
    <div class="slide" role="img" aria-label="Close-up photograph of a green circuit board with chips and resistors">
      <h1 class="l1">COMMERCIAL - INDUSTRIAL - DOMESTIC</h1>
      <h1 class="l2">ELECTRICAL INSTALLATIONS</h1>
      <div class="dots"><i class="on"></i><i></i><i></i></div>
    </div>
  </div>
  <section class="abs welcome">
    <h2>Welcome to Fenwold Electrical</h2>
    <div class="body-copy intro">
      <div class="photo"><div role="img" aria-label="Photograph of light bulbs with one lit energy-saving bulb"></div></div>
      <p><b>Established in 2005 Fenwold Electrical Services Limited is an independent company that has grown steadily over that period into a respected Commercial and Domestic Electrical installer providing it's services nationwide.</b></p>
      <p>Professional and reliable, the secret of our success has come from recommendations from our customer base. Our staffing levels allow us to be flexible enough to tackle any size of project, contracts often exceeding 100K, yet we are able to complete the more modest budget competitively. All our work is guaranteed and our help line is always available to our clients to satisfy any after contract queries or concerns.</p>
      <p>As a company we strive to meet exceptional standards of workmanship, we are registered with the National Wiring Standards Council and all our work is certificated accordingly. All our engineers are fully qualified in their relevant fields and all work there is carried out to BS 7671 standards.</p>
      <p>As Health and safety is always such a major factor in the industry, we always ensure that at least one qualified representative is present on each site. We also employ the services of health and safety consultants on a permanent basis.</p>
    </div>
  </section>
  <div class="abs badges" aria-label="Accreditation badges"><span></span><span></span></div>
  <section class="abs services">
    <h2>Our Services</h2>
    <div class="photo"><div role="img" aria-label="Photograph of an industrial switchgear panel with isolator switches and indicator lights"></div></div>
    <div class="body-copy lead">The Company is extensively experienced throughout a broad spectrum of electrical projects, which encompass:</div>
    <ul class="service-list">
      <li>Food Industry</li><li>Retail Premises</li><li>Councils</li><li>Schools and Colleges</li>
    </ul>
    <div class="body-copy">
      <p>Further more we carryout system testing, faultfinding and survey reports.</p>
      <p>We also specialise in fire alarm inspection and testing reports.</p>
    </div>
  </section>
  <footer class="abs footer">
    <div class="copy">Copyright © 2005-2012. All rights reserved</div>
    <div class="addr">Unit 4b Commerce Way, Harbour Rd, DN40 2QX<br>Tel: 01632 960411</div>
    <div class="follow">Follow us on <i></i></div>
  </footer>
</div>
</body>
</html>
```